Quillmere Surgical Clinic ,Perth- Australia

We need a letterhead for our surgical clinic , it needs to highlight all the relevant contact details and practice locations. needs to be eye catching, but remain professional.all the logos attached
clear contact details as follows

Surgeon name : Mr Tevin Oskard
Phone : 1300 482 917 - 0417 296 481
Fax : 08- 7524 3968
email : tevin@parvellaclinicgroup.com.au
www.parvellaclinicgroup.com.au

Consults from
1- Haldane Medical Centre - Level 3 - Suite 42.
9 Cotterill Vance Parade
Murdoch WA 6157

2- KBRT Mandurah Suites
54 Pellingham Road Mandurah 6214

Operates at :
Our Lady of Peace Murdoch Hospital
Doreen Whitcombe Hospital
Tarn Health Campus
Rookwell Hospital
Ravenfield Hopital
Our Lady of Peace Subiaco

Target Market(s)

General Practitioners (Family doctors)

Industry/Entity Type

Medical

Requirements
Must have
• all the logos attached
• clear contact details as follows
• Surgeon name : Mr Tevin Oskard
• Phone : 1300 482 917 - 0417 296 481
• Fax : 08- 7524 3968
• email : tevin@parvellaclinicgroup.com.au
• www.parvellaclinicgroup.com.au
• Consults from
• 1- Haldane Medical Centre - Level 3 - Suite 42.
• 9 Cotterill Vance Parade
• Murdoch WA 6157
• 2- KBRT Mandurah Suites
• 54 Pellingham Road Mandurah 6214
• Operates at :
• Our Lady of Peace Murdoch Hospital
• Doreen Whitcombe Hospital
• Tarn Health Campus
• Rookwell Hospital
• Ravenfield Hopital
• Our Lady of Peace Subiaco
Nice to have
• a surgical theme in the design , but remain professional
Should not have
• big chunky designs
• no photographs or diagrams of objects (ECG, or stethoscope ..ect)

```html
<!DOCTYPE html>
<html lang="en">
<head>
<meta charset="utf-8">
<title>Quillmere Surgical Clinic – Letterhead</title>
<link rel="stylesheet" href="https://fonts.googleapis.com/css2?family=Cabin+Condensed:wght@400;500&display=swap">
<style>
  :root {
    --backdrop: #e4e4e6;
    --paper: #ffffff;
    --navy: #1d4f8c;
    --clinic-blue: #1f5d9c;
    --accent-red: #a51e1e;
    --band-blue: #2a80bf;
    --ring-blue: #a9cde0;
    --watermark: #f1f4f8;
    --badge-navy: #2a3f8f;
    --badge-grey: #d9dce3;
    --badge-sky: #9fd3e0;
    --badge-pink: #e7a7c4;
  }
  * { margin: 0; padding: 0; box-sizing: border-box; }
  html, body { width: 1200px; height: 991px; overflow: hidden; background: var(--backdrop); }
  body { font-family: "Cabin Condensed", sans-serif; position: relative; }

  .letterhead {
    position: absolute; left: 261px; top: 20px;
    width: 678px; height: 951px;
    background: var(--paper);
    box-shadow: 0 2px 8px rgba(0,0,0,.12);
    overflow: hidden;
  }
  .letterhead > * { position: absolute; }

  .brand-ring {
    left: 70px; top: 29px; width: 92px; height: 92px;
    border-radius: 50%; border: 5px solid var(--ring-blue);
  }
  .brand-name {
    left: 170px; top: 41px; width: 145px;
    text-align: center; color: var(--clinic-blue);
    font-size: 18.5px; font-weight: 500; letter-spacing: 2.6px; line-height: 24px;
    text-transform: uppercase;
  }

  .surgeon { left: 439px; top: 40px; color: var(--navy); }
  .surgeon-name { font-size: 13.5px; font-weight: 500; margin-bottom: 2px; }
  .contact-line { font-size: 10.5px; line-height: 13px; display: flex; align-items: center; gap: 4px; }
  .contact-line svg { width: 9px; height: 9px; flex: none; }

  .rule { left: 63px; width: 564px; height: 2px; background: var(--accent-red); }
  .rule-top { top: 134px; }
  .rule-bottom { top: 263px; }

  .locations h2 { color: var(--accent-red); font-size: 15px; font-weight: 500; margin-bottom: 5px; }
  .locations p { color: var(--navy); font-size: 10.5px; line-height: 13px; }
  .locations .gap { margin-top: 3px; }
  .consults { left: 69px; top: 141px; }
  .consults p + p.block { margin-top: 6px; }
  .operates { left: 465px; top: 141px; }
  .operates p { line-height: 14px; }

  .watermark-ring {
    left: 119px; top: 334px; width: 426px; height: 426px;
    border-radius: 50%; border: 18px solid var(--watermark);
  }

  .badge { background: var(--badge-grey); }
  .badge-seal { left: 73px; top: 840px; width: 60px; height: 60px; border-radius: 50%; background: var(--badge-navy); }
  .badge-college { left: 151px; top: 856px; width: 115px; height: 36px; border-radius: 3px; }
  .badge-association { left: 292px; top: 848px; width: 115px; height: 44px; border-radius: 3px; }
  .badge-breast { left: 436px; top: 839px; width: 85px; height: 24px; border-radius: 3px; background: var(--badge-pink); opacity: .7; }
  .badge-oncology { left: 436px; top: 870px; width: 85px; height: 30px; border-radius: 3px; }
  .badge-endocrine { left: 531px; top: 842px; width: 52px; height: 58px; border-radius: 3px; background: var(--badge-sky); opacity: .6; }
  .badge-general { left: 595px; top: 845px; width: 33px; height: 56px; background: var(--clinic-blue); }

  .footer-rule { left: 0; top: 906px; width: 100%; height: 3px; background: var(--accent-red); }
  .footer-band { left: 0; top: 914px; width: 100%; height: 37px; background: var(--band-blue); }
</style>
</head>
<body>
  <main class="letterhead">
    <div class="brand-ring" aria-hidden="true"></div>
    <div class="brand-name">Quillmere<br>Surgical<br>Clinic</div>

    <section class="surgeon">
      <p class="surgeon-name">Mr Tevin Oskard</p>
      <p class="contact-line">
        <svg viewBox="0 0 10 10"><rect width="10" height="10" rx="2" fill="#a51e1e"/><path d="M3 2.5h1.5l.5 1.5-1 .7a4 4 0 0 0 1.3 1.3l.7-1 1.5.5V7a1 1 0 0 1-1 .5A5 5 0 0 1 2.5 3.5 1 1 0 0 1 3 2.5z" fill="#fff"/></svg>
        1300 482 917 - 0417 296 481
      </p>
      <p class="contact-line">
        <svg viewBox="0 0 10 10"><rect x="2.5" y="0.5" width="5" height="3" fill="#a51e1e"/><rect x="0.5" y="3.5" width="9" height="4" rx="1" fill="#a51e1e"/><rect x="2.5" y="6" width="5" height="3.5" fill="#a51e1e" stroke="#fff" stroke-width=".6"/></svg>
        08- 7524 3968
      </p>
      <p class="contact-line">
        <svg viewBox="0 0 10 10"><rect x="0.5" y="2" width="9" height="6.5" fill="#a51e1e"/><path d="M.5 2l4.5 3.5L9.5 2" fill="none" stroke="#fff" stroke-width=".8"/></svg>
        tevin@parvellaclinicgroup.com.au
      </p>
      <p class="contact-line">
        <svg viewBox="0 0 10 10" fill="none" stroke="#a51e1e" stroke-width=".8"><circle cx="5" cy="5" r="4.4"/><ellipse cx="5" cy="5" rx="2" ry="4.4"/><path d="M.6 5h8.8M1.5 2.8h7M1.5 7.2h7"/></svg>
        www.parvellaclinicgroup.com.au
      </p>
    </section>

    <div class="rule rule-top"></div>

    <section class="locations consults">
      <h2>Consults From</h2>
      <p>Haldane Medical Centre</p>
      <p>Level 3 - Suite 42</p>
      <p class="block">9 Cotterill Vance Parade</p>
      <p>Murdoch WA 6157</p>
      <p class="block" style="margin-top:8px">KBRT Mandurah Suites</p>
      <p>54 Pellingham Road Mandurah 6214</p>
    </section>

    <section class="locations operates">
      <h2>Operates at :</h2>
      <p>Our Lady of Peace Murdoch Hospital</p>
      <p>Doreen Whitcombe Hospital</p>
      <p>Tarn Health Campus</p>
      <p>Rookwell Hospital</p>
      <p>Ravenfield Hopital</p>
      <p>Our Lady of Peace Subiaco</p>
    </section>

    <div class="rule rule-bottom"></div>

    <div class="watermark-ring" aria-hidden="true"></div>

    <div class="badge-seal" role="img" aria-label="Professional society badge"></div>
    <div class="badge badge-college" role="img" aria-label="Surgical college fellowship badge"></div>
    <div class="badge badge-association" role="img" aria-label="Surgical association badge"></div>
    <div class="badge-breast" role="img" aria-label="Breast surgeons society badge"></div>
    <div class="badge badge-oncology" role="img" aria-label="Clinical oncology society badge"></div>
    <div class="badge-endocrine" role="img" aria-label="Endocrine surgeons society badge"></div>
    <div class="badge-general" role="img" aria-label="General surgeons society badge"></div>

    <div class="footer-rule"></div>
    <div class="footer-band"></div>
  </main>
</body>
</html>
```